VELVET ORBITS - BOOK COVER

I have written a book called VELVET ORBIT - HOW TO CLIMB PAST EVERY LIMIT TO THE TOP RUNG. I need a front cover design for the book. The book cover needs to be intriguing for someone to pick it up and read the first couple of pages. I want people to think about ACHIEVING SUCCESS when they read this book.
PLEASE LOOK AT THE ATTACHMENT. THANKS!

Target Market(s)

males, entrepreneurs, small business owners, salespeople, corporate executives

Industry/Entity Type

Business

Logo Text

VELVET ORBITS

Logo styles of interest
Emblem Logo
Abstract Logo
Font styles to use
Serif
Sans Serif

Colors
ec1f27
000000
959595
ffffff

Requirements
Must have
• It has to have a "hurricane" feel to it with hurricane colors.
Nice to have
• I open to your ideas
Should not have
• no other colors except red, black, gray, white.

```html
<!DOCTYPE html>
<html lang="en">
<head>
<meta charset="utf-8">
<title>Velvet Orbit – Book Cover</title>
<link rel="stylesheet" href="https://fonts.googleapis.com/css2?family=Cinzel:wght@400;500&display=swap">
<style>
  :root {
    --red: #ec1f27;
    --black: #000000;
    --gray: #959595;
    --white: #ffffff;
    --backdrop: #ececec;
    --storm-red: rgba(236, 31, 39, 0.14);
    --storm-gray: rgba(149, 149, 149, 0.22);
  }
  * { margin: 0; padding: 0; box-sizing: border-box; }
  html, body {
    width: 1200px;
    height: 800px;
    overflow: hidden;
    background: var(--backdrop);
  }
  .stage {
    width: 1200px;
    height: 800px;
    display: flex;
    align-items: center;
    justify-content: center;
  }
  .cover {
    position: relative;
    width: 500px;
    height: 730px;
    background: var(--white);
    font-family: "Cinzel", serif;
    text-align: center;
    overflow: hidden;
  }
  .cover__storm {
    position: absolute;
    inset: 0;
    background:
      radial-gradient(ellipse 210px 260px at 200px 250px, var(--storm-red) 0%, rgba(236, 31, 39, 0.05) 60%, transparent 100%),
      radial-gradient(ellipse 230px 300px at 300px 500px, var(--storm-gray) 0%, rgba(149, 149, 149, 0.08) 60%, transparent 100%);
  }
  .cover__title {
    position: absolute;
    top: 80px;
    left: 0;
    right: 0;
    font-size: 40px;
    font-weight: 400;
    letter-spacing: 0.5px;
    color: var(--black);
  }
  .cover__title-accent { color: var(--red); }
  .cover__mark {
    position: absolute;
    top: 180px;
    left: 0;
    right: 0;
    display: flex;
    align-items: center;
    justify-content: center;
    gap: 14px;
  }
  .cover__mark-dot {
    width: 64px;
    height: 64px;
    border-radius: 50%;
    background: var(--red);
  }
  .cover__mark-name {
    font-size: 20px;
    font-weight: 400;
    letter-spacing: 2px;
    color: var(--black);
  }
  .cover__subtitle {
    position: absolute;
    top: 330px;
    left: 0;
    right: 0;
    font-size: 25px;
    font-weight: 400;
    line-height: 1.4;
  }
  .cover__subtitle-line--red { display: block; color: var(--red); }
  .cover__subtitle-line--black { display: block; color: var(--black); }
  .cover__author {
    position: absolute;
    top: 552px;
    left: 0;
    right: 0;
    font-size: 16px;
    font-weight: 400;
    letter-spacing: 0.5px;
    color: var(--red);
  }
</style>
</head>
<body>
  <main class="stage">
    <article class="cover">
      <div class="cover__storm" role="img" aria-label="Faint red and gray swirling storm motif filling the cover background"></div>

      <h1 class="cover__title">VELVET <span class="cover__title-accent">ORBIT</span></h1>

      <div class="cover__mark">
        <span class="cover__mark-dot" aria-hidden="true"></span>
        <span class="cover__mark-name">VELVET ORBITS</span>
      </div>

      <h2 class="cover__subtitle">
        <span class="cover__subtitle-line--red">HOW TO CLIMB PAST EVERY LIMIT</span>
        <span class="cover__subtitle-line--black">TO THE TOP RUNG</span>
      </h2>

      <p class="cover__author">BY CALE WINTERROD</p>
    </article>
  </main>
</body>
</html>
```